General Dental Office Business Card

I run a private general dental office in southern California, and would like a refresh/redesign of my business card. I focus on quality care rather than volume. The email address on the uploaded current card should be updated to: info@marbleshoredental.example. The current card's logo is a deboss, but I am open to other ideas. The logo can be refreshed, but it is something that's been with me since the beginning of the office, so I wouldn't want a drastic redesign.
Target Market(s)
Adults 18-99, whoever needs dental services
Industry/Entity Type
Healthcare/Dental
Contact Information for Business Card
Name, Address, Phone, email
Colors
Designer to choose colors to be used in the design.
Requirements
Must have
- Logo (Same as original one in the uploaded file), space on back for appointment time/date

```html
<!DOCTYPE html>
<html lang="en">
<head>
<meta charset="utf-8">
<title>Marble Shore Dental – Business Card</title>
<link rel="stylesheet" href="https://fonts.googleapis.com/css2?family=Nunito+Sans:ital,wght@0,400;0,600;0,700;1,300&family=Source+Sans+3:wght@400&display=swap">
<style>
  :root {
    --aqua: #55d9f8;
    --white: #ffffff;
    --ink: #6d6e70;
    --rule: #6d6e70;
    --stage: #000000;
  }
  * { box-sizing: border-box; margin: 0; padding: 0; }
  html, body { width: 1200px; height: 1199px; overflow: hidden; background: var(--stage); }
  body { position: relative; font-family: "Nunito Sans", sans-serif; }

  .card {
    position: absolute;
    top: 209px;
    width: 429px;
    height: 771px;
    overflow: hidden;
  }
  .card--back { left: 142px; background: var(--aqua); }
  .card--front { left: 611px; background: var(--white); }

  /* back side */
  .back-mark {
    position: absolute; left: 95px; top: 101px;
    width: 240px; height: 240px; border-radius: 50%;
    background: var(--white);
    display: flex; align-items: center; justify-content: center;
  }
  .back-mark__name {
    color: var(--aqua); font-weight: 700; font-size: 26px;
    text-align: center; line-height: 1.15; width: 180px;
  }
  .back-web {
    position: absolute; left: 0; right: 0; top: 388px;
    text-align: center; color: var(--white);
    font-family: "Source Sans 3", sans-serif; font-size: 24px; letter-spacing: 0.5px;
  }
  .back-water {
    position: absolute; left: 0; right: 0; top: 460px; height: 150px;
    background: linear-gradient(to bottom, var(--aqua) 0%, #a6ecfb 55%, var(--white) 100%);
  }
  .back-lower {
    position: absolute; left: 0; right: 0; top: 610px; bottom: 0;
    background: var(--white);
  }
  .appt-field {
    position: absolute; left: 44px; width: 335px;
    border-top: 1.5px solid var(--rule);
    text-align: center; color: var(--ink);
    font-size: 19px; padding-top: 2px;
  }
  .appt-field--date { top: 632px; }
  .appt-field--time { top: 709px; }

  /* front side */
  .front-mark {
    position: absolute; left: 129px; top: 51px;
    width: 170px; height: 170px; border-radius: 50%;
    background: var(--aqua);
  }
  .front-title {
    position: absolute; left: 0; right: 0; top: 228px;
    text-align: center; color: var(--aqua);
    font-weight: 700; font-size: 39px; letter-spacing: 0.3px;
  }
  .front-person { position: absolute; right: 42px; top: 334px; text-align: right; color: var(--ink); }
  .front-person__name { font-weight: 400; font-size: 31px; line-height: 1.15; }
  .front-person__role { font-style: italic; font-weight: 300; font-size: 21px; line-height: 1.2; }

  .contact-list { position: absolute; left: 40px; top: 465px; list-style: none; }
  .contact-list li {
    display: flex; align-items: center; height: 30.6px;
    font-family: "Source Sans 3", sans-serif; font-size: 18px; color: var(--ink);
  }
  .contact-list svg { width: 21px; height: 21px; margin-right: 10px; flex: none; }
  .front-water {
    position: absolute; left: 0; right: 0; top: 625px; bottom: 0;
    background: linear-gradient(to bottom, var(--white) 0%, #a6ecfb 45%, var(--aqua) 100%);
  }
</style>
</head>
<body>

<section class="card card--back">
  <div class="back-mark"><div class="back-mark__name">Marble Shore Dental</div></div>
  <div class="back-web">www.marbleshoredental.example</div>
  <div class="back-water" role="img" aria-label="Brushed water ripple texture fading from aqua to white"></div>
  <div class="back-lower"></div>
  <div class="appt-field appt-field--date">Appointment Date</div>
  <div class="appt-field appt-field--time">Time</div>
</section>

<section class="card card--front">
  <div class="front-mark"></div>
  <h1 class="front-title">Marble Shore Dental</h1>
  <div class="front-person">
    <div class="front-person__name">Daniel R. Moss DDS</div>
    <div class="front-person__role">General Dentistry</div>
  </div>
  <ul class="contact-list">
    <li>
      <svg viewBox="0 0 20 20" aria-hidden="true"><circle cx="10" cy="10" r="10" fill="var(--aqua)"/><path d="M4.5 10.5 10 5l5.5 5.5M6.5 9v5.5h7V9" fill="var(--white)" stroke="var(--white)" stroke-width="1.2" stroke-linejoin="round"/><rect x="9" y="11" width="2" height="3.5" fill="var(--aqua)"/></svg>
      1820 Harbor Crest Way Seaview, CA 92000
    </li>
    <li>
      <svg viewBox="0 0 20 20" aria-hidden="true"><circle cx="10" cy="10" r="10" fill="var(--aqua)"/><path d="M7 5.5c-1 .5-1.6 1.4-1.2 2.8.9 2.8 3 5 5.9 6 1.3.4 2.2-.2 2.7-1.2l-1.8-1.6-1.2.8c-1.2-.6-2.1-1.6-2.7-2.8l.8-1.2z" fill="var(--white)"/></svg>
      555-014-7391
    </li>
    <li>
      <svg viewBox="0 0 20 20" aria-hidden="true"><circle cx="10" cy="10" r="10" fill="var(--aqua)"/><rect x="5" y="6.5" width="10" height="7" fill="none" stroke="var(--white)" stroke-width="1.2"/><path d="M5 6.5l5 4 5-4M5 13.5l3.7-3.5M15 13.5l-3.7-3.5" fill="none" stroke="var(--white)" stroke-width="1.1"/></svg>
      email:&nbsp; info@marbleshoredental.example
    </li>
    <li>
      <svg viewBox="0 0 20 20" aria-hidden="true"><circle cx="10" cy="10" r="10" fill="var(--aqua)"/><g fill="none" stroke="var(--white)" stroke-width="1.1"><circle cx="10" cy="10" r="5.5"/><ellipse cx="10" cy="10" rx="2.4" ry="5.5"/><path d="M4.5 10h11M5.5 7h9M5.5 13h9"/></g></svg>
      web:&nbsp; www.marbleshoredental.example
    </li>
  </ul>
  <div class="front-water" role="img" aria-label="Brushed water ripple texture deepening from white to aqua"></div>
</section>

</body>
</html>
```